Steadfast Valve Works

I need a business card with the attached logo.
The second page I have attached is what we are looking for. We want doubles sided. We would like the blues fading and the logo on the back.

Industry/Entity Type

Business

```html
<!DOCTYPE html>
<html lang="en">
<head>
<meta charset="utf-8">
<title>Steadfast Valve Works – Business Card</title>
<link href="https://fonts.googleapis.com/css2?family=Michroma&display=swap" rel="stylesheet">
<style>
  :root {
    --backdrop: #e6e6e6;
    --card: #ffffff;
    --brand-blue: #0d3f94;
    --brand-blue-deep: #0a3580;
    --band-shadow: #8e8e8e;
    --ink: #4a4a4a;
    --ink-soft: #6a6a6a;
    --rule: #b5b5b5;
  }
  * { box-sizing: border-box; margin: 0; padding: 0; }
  html, body {
    width: 1200px; height: 900px; overflow: hidden;
    background: var(--backdrop);
  }
  .card {
    position: absolute; left: 180px; top: 210px;
    width: 840px; height: 480px;
    background: var(--card);
    box-shadow: 0 12px 30px rgba(0,0,0,0.18);
    overflow: hidden;
    font-family: 'Michroma', sans-serif;
    color: var(--ink);
  }
  .brand-name {
    position: absolute; left: 140px; top: 92px;
    font-family: 'Michroma', sans-serif;
    font-size: 30px; letter-spacing: 2px;
    color: var(--brand-blue);
    text-transform: uppercase;
    white-space: nowrap;
  }
  .person {
    position: absolute; left: 110px; top: 190px; width: 250px;
    text-align: right;
  }
  .person-name { font-size: 15px; letter-spacing: 2px; text-transform: uppercase; color: var(--ink); }
  .person-title { font-size: 11px; letter-spacing: 2px; margin-top: 8px; color: var(--ink-soft); text-transform: uppercase; }
  .address {
    position: absolute; left: 60px; top: 272px; width: 300px;
    text-align: right; font-size: 11px; letter-spacing: 2px; line-height: 1.9;
    color: var(--ink-soft); text-transform: uppercase;
  }
  .divider {
    position: absolute; left: 385px; top: 170px;
    width: 1px; height: 150px; background: var(--rule);
  }
  .contacts {
    position: absolute; left: 410px; top: 168px;
    list-style: none; font-size: 12px; letter-spacing: 1.5px;
    color: var(--ink);
  }
  .contacts li { display: flex; align-items: center; gap: 10px; height: 24px; white-space: nowrap; }
  .contacts .gap { height: 12px; }
  .contact-icon { width: 16px; height: 16px; flex: none; }
  .band { position: absolute; left: 0; bottom: 0; width: 840px; height: 180px; }
  .band-url {
    position: absolute; right: 60px; bottom: 18px;
    font-size: 13px; letter-spacing: 3px; color: #ffffff; text-transform: uppercase;
    white-space: nowrap;
  }
</style>
</head>
<body>
  <section class="card" aria-label="Business card front">
    <div class="brand-name">Steadfast Valve Works</div>

    <div class="person">
      <div class="person-name">Daniel Reyes</div>
      <div class="person-title">Owner / C.E.O</div>
    </div>
    <div class="address">Suite # 410, Kell Bldg,<br>NY 10482</div>

    <div class="divider"></div>

    <ul class="contacts">
      <li>
        <svg class="contact-icon" viewBox="0 0 16 16"><circle cx="8" cy="8" r="8" fill="#4a4a4a"/><path d="M5.5 4.5c.5-.4 1-.3 1.2.2l.5 1.2c.1.3 0 .6-.3.8l-.5.4c.4 1 1.1 1.8 2.1 2.2l.4-.5c.2-.3.5-.3.8-.2l1.2.5c.5.2.6.7.2 1.2-.6.8-1.6 1-2.6.5C6.7 10 5.2 8.5 4.6 6.8c-.3-.9-.1-1.7.9-2.3z" fill="#fff"/></svg>
        555-210-4817
      </li>
      <li>
        <svg class="contact-icon" viewBox="0 0 16 16"><circle cx="8" cy="8" r="8" fill="#4a4a4a"/><rect x="5.5" y="3.5" width="5" height="9" rx="1" fill="#fff"/><rect x="6.5" y="4.8" width="3" height="5" fill="#4a4a4a"/></svg>
        555-306-9924
      </li>
      <li>
        <svg class="contact-icon" viewBox="0 0 16 16"><circle cx="8" cy="8" r="8" fill="#4a4a4a"/><rect x="4" y="6" width="8" height="5" rx="1" fill="#fff"/><rect x="5.5" y="3.5" width="5" height="3" fill="#fff"/></svg>
        555-472-1358
      </li>
      <li class="gap"></li>
      <li>
        <svg class="contact-icon" viewBox="0 0 16 16"><circle cx="8" cy="8" r="8" fill="#4a4a4a"/><rect x="4" y="5" width="8" height="6" fill="#fff"/><path d="M4 5l4 3.5L12 5" stroke="#4a4a4a" fill="none"/></svg>
        daniel@steadfastvalve.com
      </li>
      <li>
        <svg class="contact-icon" viewBox="0 0 16 16"><circle cx="8" cy="8" r="8" fill="#4a4a4a"/><circle cx="8" cy="8" r="4.5" stroke="#fff" fill="none"/><path d="M3.5 8h9M8 3.5c-2 2.5-2 6.5 0 9M8 3.5c2 2.5 2 6.5 0 9" stroke="#fff" fill="none" stroke-width="0.8"/></svg>
        www.steadfastvalve.com
      </li>
    </ul>

    <svg class="band" viewBox="0 0 840 180" preserveAspectRatio="none" aria-hidden="true">
      <defs>
        <linearGradient id="bandFade" x1="0" y1="0" x2="1" y2="0">
          <stop offset="0" stop-color="#0a3580"/>
          <stop offset="1" stop-color="#0d3f94"/>
        </linearGradient>
      </defs>
      <path d="M0 180 C 300 164, 560 92, 840 32 L 840 180 Z" fill="var(--band-shadow)"/>
      <path d="M0 180 C 300 172, 560 110, 840 50 L 840 180 Z" fill="url(#bandFade)"/>
    </svg>
    <div class="band-url">www.steadfastvalve.com</div>
  </section>
</body>
</html>
```